Business Card Design Harbor of Calm

mental health provider
contemporary
warmth
inviting

Target Market(s)

mental health clients adults

Industry/Entity Type

Mental Health

Contact Information for Business Card

Danielle Arkwright PMHNP
2841 SW Tenley Ave
Suite 384C
Portland OR 97318
Fax 503-555-0182
Tel 503-555-0147
Email danielle@darkwright.example
Website darkwright.example

Requirements
Nice to have
• see above
Should not have
• no medical logos

```html
<!DOCTYPE html>
<html lang="en">
<head>
<meta charset="utf-8">
<title>Harbor of Calm – Business Card</title>
<link href="https://fonts.googleapis.com/css2?family=Open+Sans:wght@600;700&display=swap" rel="stylesheet">
<style>
  :root {
    --sky-top: #1d5fae;
    --sky-bottom: #2a8fe2;
    --gold-light: #b8a35a;
    --gold-mid: #9c8840;
    --gold-dark: #5e4f22;
    --card-edge: #4a3d18;
    --brand-gold: #f2c14e;
    --silver-light: #ffffff;
    --silver-dark: #8d93a0;
    --ink-shadow: #1d1a10;
    --band-deep: #1a7bb8;
    --band-deep-top: #3aa3d6;
    --band-pale: #6fb3e3;
    --band-pale-top: #a9d6f4;
  }
  * { margin: 0; padding: 0; box-sizing: border-box; }
  html, body {
    width: 900px; height: 1200px; overflow: hidden;
  }
  body {
    position: relative;
    background: linear-gradient(160deg, var(--sky-top), var(--sky-bottom));
    font-family: "Open Sans", sans-serif;
  }
  .card {
    position: absolute;
    left: 15px; width: 870px; height: 506px;
    border: 2px solid var(--card-edge);
    background:
      radial-gradient(ellipse at 50% 40%, rgba(255,240,180,0.18), transparent 65%),
      linear-gradient(180deg, var(--gold-mid) 0%, var(--gold-light) 45%, var(--gold-mid) 75%, var(--gold-dark) 100%);
    box-shadow: inset 0 0 18px rgba(40,30,5,0.55);
    overflow: hidden;
  }
  .card--front { top: 60px; }
  .card--back { top: 627px; }

  .metal {
    position: absolute;
    font-weight: 700;
    white-space: nowrap;
    background: linear-gradient(180deg, var(--silver-light) 0%, #e4e7ee 45%, var(--silver-dark) 55%, #d9dde5 100%);
    -webkit-background-clip: text;
    background-clip: text;
    color: transparent;
    filter: drop-shadow(1px 2px 1px var(--ink-shadow));
  }
  .name { font-size: 40px; letter-spacing: 0.5px; text-transform: uppercase; }
  .tel { font-size: 26px; text-transform: uppercase; }
  .smallcaps { font-variant: small-caps; }

  .brand-mark {
    position: absolute;
    left: 100px; top: 120px;
    width: 250px;
    color: var(--brand-gold);
    font-weight: 700;
    font-size: 44px;
    line-height: 1.1;
    text-align: center;
  }
  .brand-mark .mark-square {
    display: block;
    width: 34px; height: 34px;
    margin: 0 auto 14px;
    background: var(--brand-gold);
  }
  .brand-echo {
    position: absolute;
    color: rgba(70,60,25,0.22);
    font-weight: 700;
    font-size: 56px;
    line-height: 1.05;
    text-align: center;
  }
  .card--front .brand-echo { left: 330px; top: 300px; width: 300px; }
  .card--back .brand-echo { left: 310px; top: 110px; width: 300px; }

  .card--front .name { left: 355px; top: 165px; }
  .card--front .tel { left: 418px; top: 215px; }
  .card--back .name { left: 42px; top: 40px; }
  .card--back .tel { left: 105px; top: 88px; }

  .address {
    position: absolute;
    left: 0; width: 870px; top: 262px;
    text-align: center;
    font-size: 33px;
    line-height: 45px;
  }
  .address .metal { position: static; display: block; }

  .band {
    position: absolute;
    left: 26px; width: 816px;
    display: flex; align-items: center; justify-content: center;
    font-size: 34px;
  }
  .band .metal { position: static; }
  .band--email {
    top: 353px; height: 46px;
    background: linear-gradient(180deg, var(--band-deep-top), var(--band-deep));
  }
  .band--web {
    top: 401px; height: 68px;
    border: 2px solid #e8f2fa;
    background: linear-gradient(180deg, var(--band-pale-top), var(--band-pale));
  }
</style>
</head>
<body>
  <section class="card card--front">
    <div class="brand-mark"><span class="mark-square"></span>Harbor of Calm</div>
    <div class="brand-echo" aria-hidden="true">Harbor of Calm</div>
    <div class="metal name">Danielle Arkwright</div>
    <div class="metal tel">Tel - 503-555-0147</div>
  </section>

  <section class="card card--back">
    <div class="brand-echo" aria-hidden="true">Harbor of Calm</div>
    <div class="metal name">Danielle Arkwright</div>
    <div class="metal tel">Tel - 503-555-0147</div>
    <div class="address smallcaps">
      <span class="metal">PMHNP 2841 SW Tenley Ave</span>
      <span class="metal">Suite 384C Portland OR 97318</span>
    </div>
    <div class="band band--email smallcaps"><span class="metal">Email - danielle@darkwright.example</span></div>
    <div class="band band--web smallcaps"><span class="metal">Website - http://darkwright.example</span></div>
  </section>
</body>
</html>
```